Ad Proposal Design

We need an Ad proposal for potential sponsors. We it similar to the attached proposal. At the top have "Expand Your Business" and our name "Gravel Lane Fellas" underneath. The word "Ad" under our name and the following logos underneath that (Pictora, Gatherly, ClipVane, Bramble Podcast, and Tunexa)

"Our Analytics" section next similar to the black picture attached but instead of the bar graph use a line graph with the line starting at the bottom left corner and ending with an arrow skyrocketing off the chart to the top right. Beside the graph have "Reach" 50,000 monthly. "Engagements" 10,000 monthly. "Radio"

In the last section "Ad Structure Models", underneath "Bright Start" $250 and "Full Circle" $500. Under the Bright Start section the following paragraphs,
"One 30-60 second Ad will be read during our weekly podcast.

Your company will have exposure to our 7000+ listeners via Bramble, Tunexa, Quorvo, ClipVane, and our Website.

Our supporters will have a chance to hear all the great things your company provides, this will increase traffic and sales."

Under the Full Circle section have the following paragraphs,
"Your company will receive all the benefits from the "Bright Start" package.

Plus you will be exposed to our entire social media platforms with over 50k accounts reached and over 10k engagements monthly. (Gatherly, Pictora, ClipVane)

Your logo will be placed in our podcast videos. You will receive 1 new piece of merch every release, 2 tickets to our live event, and a plush Gravel Lane Fellas heart for Full Circle you've shown."

Last have the following paragraph,
"Your logo will be placed on our website on our Ad/Sponsors page to provide our supporters a direct link to your business."

```html
<!DOCTYPE html>
<html lang="en">
<head>
<meta charset="utf-8">
<title>Gravel Lane Fellas Ads</title>
<link rel="stylesheet" href="https://fonts.googleapis.com/css2?family=Montserrat:wght@400;500;700;800&display=swap">
<style>
  :root {
    --brand-blue: #1a9ad6;
    --ink: #1d1d1f;
    --white: #ffffff;
    --panel-grey: #efefef;
    --panel-blue: #c4ecf8;
    --space-deep: #0b0b16;
    --space-violet: #3a2a5c;
    --grid: #e6e6e6;
  }
  * { box-sizing: border-box; margin: 0; padding: 0; }
  html, body { width: 1200px; height: 2906px; overflow: hidden; background: var(--white); }
  body { font-family: "Montserrat", Arial, sans-serif; color: var(--ink); position: relative; }

  .hero {
    position: absolute; left: 0; top: 0; width: 1200px; height: 743px;
    background:
      radial-gradient(ellipse 420px 300px at 560px 360px, rgba(120, 90, 170, 0.55), transparent 70%),
      radial-gradient(ellipse 700px 500px at 900px 200px, rgba(70, 50, 120, 0.5), transparent 70%),
      linear-gradient(160deg, var(--space-deep) 0%, var(--space-violet) 55%, #151027 100%);
    color: var(--white);
  }
  .hero-eyebrow { position: absolute; left: 80px; top: 86px; font-size: 40px; font-weight: 700; letter-spacing: 2px; }
  .hero-rule { position: absolute; left: 80px; top: 168px; width: 241px; height: 10px; background: var(--brand-blue); }
  .hero-title { position: absolute; left: 80px; top: 268px; font-size: 76px; font-weight: 800; letter-spacing: 2px; line-height: 1; }
  .hero-sub { position: absolute; left: 80px; top: 415px; font-size: 76px; font-weight: 800; letter-spacing: 2px; line-height: 1; }
  .channels { position: absolute; left: 80px; top: 610px; display: flex; gap: 34px; align-items: center; }
  .channel { display: flex; align-items: center; gap: 12px; font-size: 26px; font-weight: 700; color: var(--white); }
  .channel-dot { width: 40px; height: 40px; border-radius: 50%; background: var(--brand-blue); }

  .section-heading { position: absolute; left: 251px; width: 698px; text-align: center;
    border-top: 5px solid var(--brand-blue); border-bottom: 5px solid var(--brand-blue);
    font-size: 45px; font-weight: 800; letter-spacing: 3px; }
  .heading-models { top: 818px; height: 124px; line-height: 114px; }
  .heading-analytics { top: 2178px; height: 122px; line-height: 112px; }

  .package { position: absolute; top: 1008px; height: 937px; text-align: center; }
  .package-basic { left: 0; width: 546px; background: var(--panel-grey); }
  .package-full { left: 556px; width: 644px; background: var(--panel-blue); }
  .package-name { margin-top: 36px; font-size: 59px; font-weight: 800; color: var(--brand-blue); line-height: 72px; letter-spacing: 1px; }
  .package-body { margin: 34px auto 0; font-size: 31px; line-height: 42px; font-weight: 400; }
  .package-basic .package-body { width: 440px; }
  .package-full .package-body { width: 540px; }
  .package-body p + p { margin-top: 42px; }

  .footnote { position: absolute; left: 90px; top: 1982px; width: 1020px; text-align: center; font-size: 31px; line-height: 42px; font-weight: 500; }

  .growth-chart { position: absolute; left: 66px; top: 2360px; width: 450px; height: 460px; }

  .stats { position: absolute; left: 622px; top: 2366px; }
  .stat { position: absolute; left: 0; display: flex; align-items: center; gap: 24px; width: 560px; }
  .stat-icon { width: 96px; height: 96px; flex: none; }
  .stat-label { font-size: 44px; font-weight: 800; color: var(--brand-blue); letter-spacing: 1px; line-height: 1.1; }
  .stat-value { font-size: 31px; font-weight: 500; margin-top: 4px; }
  .stat-reach { top: 0; }
  .stat-engage { top: 164px; }
  .stat-radio { top: 348px; }
</style>
</head>
<body>

<header class="hero" role="img" aria-label="Deep space nebula backdrop in purple and black">
  <div class="hero-eyebrow">EXPAND YOUR BUSINESS</div>
  <div class="hero-rule"></div>
  <div class="hero-title">GRAVEL LANE FELLAS</div>
  <div class="hero-sub">ADS</div>
  <div class="channels">
    <span class="channel"><span class="channel-dot"></span>Pictora</span>
    <span class="channel"><span class="channel-dot"></span>Gatherly</span>
    <span class="channel"><span class="channel-dot"></span>ClipVane</span>
    <span class="channel"><span class="channel-dot"></span>Bramble Podcast</span>
    <span class="channel"><span class="channel-dot"></span>Tunexa</span>
  </div>
</header>

<h2 class="section-heading heading-models">AD STRUCTURE MODELS</h2>

<section class="package package-basic">
  <h3 class="package-name">BRIGHT START<br>$250</h3>
  <div class="package-body">
    <p>One 30-60 second Ad will be read during our weekly podcast.</p>
    <p>Your company will have exposure to our 7000+ listeners via Bramble, Tunexa, Quorvo, ClipVane, and our Website.</p>
    <p>Our supporters will have a chance to hear all the great things your company provides, this will increase traffic and sales.</p>
  </div>
</section>

<section class="package package-full">
  <h3 class="package-name">FULL CIRCLE<br>$500</h3>
  <div class="package-body">
    <p>Your company will receive all the benefits from the "Bright Start" package.</p>
    <p>Plus you will be exposed to our entire social media platforms with over 50k accounts reached and over 10k engagements monthly. (Gatherly, Pictora, ClipVane).</p>
    <p>Your logo will be placed in our podcast videos. You will receive 1 new piece of merch every release, 2 tickets to our live event, and a plush Gravel Lane Fellas heart for Full Circle you've shown.</p>
  </div>
</section>

<p class="footnote">Your logo will be placed on our website on our Ad/Sponsors page to provide our supporters a direct link to your business.</p>

<h2 class="section-heading heading-analytics">OUR ANALYTICS</h2>

<svg class="growth-chart" viewBox="0 0 450 460" aria-label="Line graph rising sharply to the top right">
  <g stroke="var(--grid)" stroke-width="1">
    <path d="M40 60H440M40 120H440M40 180H440M40 240H440M40 300H440M40 360H440M40 420H440"/>
    <path d="M100 40V440M160 40V440M220 40V440M280 40V440M340 40V440M400 40V440"/>
  </g>
  <path d="M6 10V446H440" fill="none" stroke="#444" stroke-width="3"/>
  <path d="M10 442C120 420 200 360 260 280S340 120 392 58" fill="none" stroke="var(--brand-blue)" stroke-width="10" stroke-linecap="round"/>
  <path d="M420 20L368 46L404 80Z" fill="var(--brand-blue)"/>
</svg>

<div class="stats">
  <div class="stat stat-reach">
    <svg class="stat-icon" viewBox="0 0 96 96" aria-hidden="true" fill="none" stroke="var(--brand-blue)" stroke-width="5">
      <circle cx="48" cy="48" r="40"/><circle cx="48" cy="48" r="26"/><circle cx="48" cy="48" r="11"/>
      <path d="M48 48L78 18M70 16H80V26" stroke-linecap="round"/>
    </svg>
    <div><div class="stat-label">REACH</div><div class="stat-value">50,000 monthly</div></div>
  </div>
  <div class="stat stat-engage">
    <svg class="stat-icon" viewBox="0 0 96 96" aria-hidden="true" fill="none" stroke="var(--brand-blue)" stroke-width="4">
      <path d="M48 34C40 22 22 26 26 40C30 50 48 58 48 58S66 50 70 40C74 26 56 22 48 34Z"/>
      <circle cx="20" cy="70" r="7"/><circle cx="48" cy="70" r="7"/><circle cx="76" cy="70" r="7"/>
      <path d="M8 92C8 82 32 82 32 92M36 92C36 82 60 82 60 92M64 92C64 82 88 82 88 92"/>
    </svg>
    <div><div class="stat-label">ENGAGEMENTS</div><div class="stat-value">10,000 monthly</div></div>
  </div>
  <div class="stat stat-radio">
    <svg class="stat-icon" viewBox="0 0 96 96" aria-hidden="true" fill="none" stroke="var(--brand-blue)" stroke-width="5" stroke-linecap="round">
      <circle cx="48" cy="38" r="7"/>
      <path d="M48 46V92"/>
      <path d="M32 22A22 22 0 0 0 32 54M64 22A22 22 0 0 1 64 54"/>
      <path d="M20 10A38 38 0 0 0 20 66M76 10A38 38 0 0 1 76 66"/>
    </svg>
    <div><div class="stat-label">RADIO</div></div>
  </div>
</div>

</body>
</html>
```